Website design using a wordpress template I purchased

I have purchased a wordpress template called "Vantrel" from Plumora and would like to design a website using it for a financial services company. The site simply needs to be informational about the company and a blog. Nothing too involved. The company provides paymaster / escrow services for commodity transactions. I am working on the logo currently and will have it ready to provide shortly. I can provide the content for the informational portion of the site as well. I would like some quick tutoring regarding how to administer the blog portion of the site once built.

```html
<!DOCTYPE html>
<html lang="en">
<head>
<meta charset="utf-8">
<title>Ledgerwise</title>
<link rel="stylesheet" href="https://fonts.googleapis.com/css2?family=Roboto:wght@400;500;700;900&family=Montserrat:wght@400;500;600&display=swap">
<style>
:root{
  --brand:#1b8fe6;
  --sky:#27a7e0;
  --navy:#0e2a47;
  --deep:#0b4e75;
  --amber:#f9bd5f;
  --ink:#1c1c1c;
  --white:#ffffff;
  --black:#000000;
}
*{margin:0;padding:0;box-sizing:border-box}
html,body{width:1200px;height:2440px;overflow:hidden;background:var(--white)}
body{position:relative;font-family:'Roboto',sans-serif;color:var(--ink)}
.abs{position:absolute}
.site-header{position:absolute;left:0;top:0;width:1200px;height:90px;background:var(--white)}
.brand{position:absolute;left:101px;top:26px;display:flex;align-items:center;gap:10px;font-weight:500;font-size:30px;line-height:36px;color:var(--brand)}
.brand-dot{width:14px;height:14px;border-radius:50%;background:var(--brand)}
.nav a{position:absolute;top:33px;font-size:17px;color:var(--ink);text-decoration:none}
.btn-outline{position:absolute;left:962px;top:21px;width:139px;height:46px;border:2px solid var(--sky);border-radius:23px;font-size:17px;display:flex;align-items:center;justify-content:center;color:var(--ink)}
.hero-art{position:absolute;left:0;top:90px}
.hero-kicker{left:99px;top:196px;font-size:34px;color:var(--white);font-weight:400}
.hero-title{left:97px;top:236px;font-size:96px;line-height:92px;font-weight:900;color:var(--navy);letter-spacing:-1px}
.hero-text{left:99px;top:434px;width:460px;font-size:17px;line-height:30px;color:var(--white)}
.btn{position:absolute;background:var(--amber);color:var(--white);border-radius:28px;display:flex;align-items:center;justify-content:center;box-shadow:0 4px 8px rgba(0,0,0,.18)}
.flow-line{position:absolute;width:1.5px;background:var(--sky)}
.about-title{left:567px;top:943px;font-size:34px;font-weight:700;color:var(--sky)}
.ticks{position:absolute;left:566px;top:1004px;width:560px;list-style:none}
.ticks li{position:relative;padding-left:36px;font-size:16px;line-height:30px;margin-bottom:15px}
.ticks svg{position:absolute;left:0;top:8px}
.blog-title{left:0;width:1200px;top:1514px;text-align:center;font-size:34px;font-weight:700;color:var(--white)}
.card{position:absolute;top:1582px;width:309px;height:345px;background:var(--white);border-radius:12px;box-shadow:0 4px 12px rgba(0,0,0,.12)}
.card-photo{position:absolute;left:0;top:0;width:309px;height:176px;border-radius:12px 12px 0 0}
.date-pill{position:absolute;left:8px;top:130px;width:125px;height:38px;border-radius:19px;background:var(--navy);color:var(--white);font-family:'Montserrat',sans-serif;font-size:11px;font-weight:500;display:flex;align-items:center;justify-content:center}
.card h3{position:absolute;left:0;width:309px;top:192px;text-align:center;font-size:26px;font-weight:500;color:var(--ink)}
.card p{position:absolute;left:0;width:309px;top:237px;text-align:center;font-family:'Montserrat',sans-serif;font-size:17px;line-height:30px;color:#333}
.card .btn{left:83px;top:317px;width:143px;height:42px;font-size:17px;border-radius:21px}
.footer-brand{left:0;width:1200px;top:2160px;display:flex;justify-content:center;align-items:center;gap:14px;font-size:56px;line-height:64px;font-weight:500;color:var(--brand)}
.footer-brand .brand-dot{width:22px;height:22px}
.footer-contact{font-size:18px;color:var(--white);display:flex;align-items:center;gap:12px}
.footer-nav a{position:absolute;top:2277px;font-size:17px;font-weight:500;color:var(--white);text-decoration:none}
.rule{left:98px;top:2344px;width:1003px;height:1.5px;background:#cfcfcf}
.legal{left:101px;top:2369px;font-size:16px;color:var(--white)}
.social{left:853px;top:2369px;font-size:16px;color:var(--white);display:flex;align-items:center;gap:14px}
.social span.dot{width:14px;height:14px;border-radius:50%;background:var(--white);display:inline-block}
</style>
</head>
<body>

<header class="site-header">
  <div class="brand"><span class="brand-dot"></span><span>Ledgerwise</span></div>
  <nav class="nav">
    <a style="left:576px">Home</a>
    <a style="left:660px">About Us</a>
    <a style="left:768px">Our Blog</a>
    <a style="left:872px">Financial</a>
  </nav>
  <div class="btn-outline">Contact Us</div>
</header>

<svg class="hero-art" width="1200" height="720" viewBox="0 90 1200 720">
  <defs>
    <linearGradient id="heroFill" x1="0" y1="0" x2="1" y2="1">
      <stop offset="0" stop-color="#b8b53a"/>
      <stop offset=".4" stop-color="#6f8a3c"/>
      <stop offset=".75" stop-color="#8f7a3c"/>
      <stop offset="1" stop-color="#c49a4a"/>
    </linearGradient>
  </defs>
  <path role="img" aria-label="Photo of a hand placing a coin on rising stacks of gold coins" d="M0 90H1200V700Q600 870 0 712Z" fill="url(#heroFill)"/>
  <path d="M0 712Q600 870 1200 700" fill="none" stroke="var(--deep)" stroke-width="9"/>
</svg>

<div class="abs hero-kicker">WELCOME TO</div>
<div class="abs hero-title">Financial<br>Services</div>
<p class="abs hero-text">Lumen Path (LP) Fellowship supports visionary and entrepreneurial Christians aiming to improve the lives of people in the developing world.</p>
<div class="btn" style="left:99px;top:550px;width:181px;height:52px;font-size:18px">Get Started</div>

<div class="flow-line" style="left:601px;top:779px;height:67px"></div>
<svg class="abs" style="left:594px;top:850px" width="15" height="14" viewBox="0 0 15 14"><path d="M2 2l5.5 5 5.5-5M2 7l5.5 5 5.5-5" fill="none" stroke="var(--sky)" stroke-width="1.6"/></svg>

<svg class="abs" style="left:52px;top:901px" width="480" height="480" viewBox="0 0 480 480">
  <circle cx="240" cy="240" r="231" fill="var(--sky)" stroke="var(--deep)" stroke-width="18" role="img" aria-label="Photo of a smiling businessman working on a laptop"/>
</svg>

<h2 class="abs about-title">ABOUT US</h2>
<ul class="ticks">
  <li><svg width="14" height="14" viewBox="0 0 14 14"><circle cx="7" cy="7" r="7" fill="var(--deep)"/><path d="M3.8 7.2l2.2 2.1 4.2-4.3" fill="none" stroke="#fff" stroke-width="1.7"/></svg>Lorem ipsum dolor sit amet, consectetur adipiscing elit, sed do eiusmod tempor incididunt ut labore et dolore magna aliqua.</li>
  <li><svg width="14" height="14" viewBox="0 0 14 14"><circle cx="7" cy="7" r="7" fill="var(--deep)"/><path d="M3.8 7.2l2.2 2.1 4.2-4.3" fill="none" stroke="#fff" stroke-width="1.7"/></svg>Lorem ipsum dolor sit amet, consectetur adipiscing elit, sed do eiusmod tempor incididunt ut labore et dolore magna aliqua.</li>
  <li style="padding-right:30px"><svg width="14" height="14" viewBox="0 0 14 14"><circle cx="7" cy="7" r="7" fill="var(--deep)"/><path d="M3.8 7.2l2.2 2.1 4.2-4.3" fill="none" stroke="#fff" stroke-width="1.7"/></svg>Lorem ipsum dolor sit amet, consectetur adipiscing elit, sed do eiusmod tempor incididunt ut labore et dolore magna aliqua. Ut enim ad minim veniam, quis nostrud exercitation ullamco laboris nisi ut aliquip ex ea commodo consequat.</li>
</ul>
<div class="btn" style="left:566px;top:1304px;width:181px;height:52px;font-size:21px">Contact Us</div>

<svg class="abs" style="left:0;top:1455px" width="1200" height="380" viewBox="0 1455 1200 380">
  <path d="M0 1525Q600 1400 1200 1525V1788Q1000 1830 600 1828Q200 1830 0 1788Z" fill="var(--sky)"/>
</svg>
<div class="flow-line" style="left:598px;top:1383px;height:104px"></div>
<svg class="abs" style="left:591px;top:1487px" width="15" height="14" viewBox="0 0 15 14"><path d="M2 2l5.5 5 5.5-5M2 7l5.5 5 5.5-5" fill="none" stroke="var(--white)" stroke-width="1.6"/></svg>
<h2 class="abs blog-title">OUR BLOG</h2>

<article class="card" style="left:99px">
  <div class="card-photo" role="img" aria-label="Photo of colleagues meeting in a bright office" style="background:linear-gradient(135deg,#c9c4bb,#6d665e)"></div>
  <div class="date-pill">OCT &nbsp;20 2022</div>
  <h3>DOLOR SIT</h3>
  <p>Lorem ipsum dolor sit amet,<br>consecteturadipiscing elit,</p>
  <div class="btn">Read More</div>
</article>
<article class="card" style="left:446px">
  <div class="card-photo" role="img" aria-label="Photo of a team discussing work at a desk" style="background:linear-gradient(135deg,#b9c2c9,#4b5663)"></div>
  <div class="date-pill">OCT &nbsp;20 2022</div>
  <h3>DOLOR SIT</h3>
  <p>Lorem ipsum dolor sit amet,<br>consecteturadipiscing elit,</p>
  <div class="btn">Read More</div>
</article>
<article class="card" style="left:791px">
  <div class="card-photo" role="img" aria-label="Photo of business partners talking in a modern office" style="background:linear-gradient(135deg,#9fae98,#3d4650)"></div>
  <div class="date-pill">OCT &nbsp;20 2022</div>
  <h3>DOLOR SIT</h3>
  <p>Lorem ipsum dolor sit amet,<br>consecteturadipiscing elit,</p>
  <div class="btn">Read More</div>
</article>

<footer>
  <svg class="abs" style="left:0;top:2030px" width="1200" height="410" viewBox="0 2030 1200 410">
    <path d="M0 2130Q600 1940 1200 2130V2440H0Z" fill="var(--black)"/>
  </svg>
  <div class="abs footer-brand"><span class="brand-dot"></span><span>Ledgerwise</span></div>
  <div class="abs footer-contact" style="left:99px;top:2181px">
    <svg width="22" height="16" viewBox="0 0 22 16"><rect x="1" y="1" width="20" height="14" rx="1.5" fill="none" stroke="#fff" stroke-width="1.6"/><path d="M1.5 2l9.5 7 9.5-7" fill="none" stroke="#fff" stroke-width="1.6"/></svg>
    <span>hello@ledgerwise.example</span>
  </div>
  <div class="abs footer-contact" style="left:869px;top:2192px;font-size:20px">
    <svg width="18" height="18" viewBox="0 0 24 24"><path d="M6.6 10.8a15.1 15.1 0 006.6 6.6l2.2-2.2a1 1 0 011-.25 11.4 11.4 0 003.6.57 1 1 0 011 1V20a1 1 0 01-1 1A17 17 0 013 4a1 1 0 011-1h3.5a1 1 0 011 1c0 1.250.2 2.45.57 3.57a1 1 0 01-.25 1z" fill="#fff"/></svg>
    <span>+1 555-014-2290</span>
  </div>
  <nav class="footer-nav">
    <a style="left:418px">Home</a>
    <a style="left:502px">About Us</a>
    <a style="left:610px">Our Blog</a>
    <a style="left:713px">Financial</a>
  </nav>
  <div class="abs rule"></div>
  <div class="abs legal">© copyrights 2022 Ledgerwise | &nbsp;All Rights Reserved</div>
  <div class="abs social">
    <span>Sociale media:</span>
    <span class="dot" aria-label="Social network 1"></span>
    <span class="dot" aria-label="Social network 2"></span>
    <span class="dot" aria-label="Social network 3"></span>
    <span class="dot" aria-label="Social network 4"></span>
  </div>
</footer>

</body>
</html>
```